Menu Board

Hi Marlene,

I would like you to design for me a menu board for all my products.

The layout I have hand drawn for you so just follow my layout.

Pho
Noodle salads
Rice
StirFry with Thick Rice Noodles
Spring Rolls Ricepaper Rolls

Poster Size: AO Vertical ( 841W x 1189H)

There are more photos of the rice dishes but I thought I can send this through so you can start and I can send you the rest of the photos when I get back from my photographer.

I will have items descriptions to follow also

• Here are the rest of the photos >

```html
<!DOCTYPE html>
<html lang="en">
<head>
<meta charset="utf-8">
<title>Menu Board</title>
<link href="https://fonts.googleapis.com/css2?family=Jost:wght@500;600;700&display=swap" rel="stylesheet">
<style>
  :root {
    --bg-light: #fbfcf7;
    --bg-mid: #e9ecdd;
    --bg-edge: #d3d8c0;
    --stripe: rgba(255,255,255,0.35);
    --band: #050505;
    --band-text: #ffffff;
    --divider: #ffffff;
    --title: #0a0a0a;
    --broth: #8a5a2a;
    --herb: #4f8a2e;
    --bowl: #f4f4f2;
    --rice: #f1ede4;
    --fried: #e9c7a0;
    --roll-fried: #c87a3a;
    --roll-fresh: #e2ecd8;
  }
  * { margin: 0; padding: 0; box-sizing: border-box; }
  html, body { width: 772px; height: 1200px; overflow: hidden; }
  body { font-family: "Jost", "Century Gothic", sans-serif; }
  .board {
    position: relative;
    width: 772px;
    height: 1200px;
    overflow: hidden;
    background:
      repeating-linear-gradient(60deg, transparent 0 14px, var(--stripe) 14px 16px),
      radial-gradient(ellipse 70% 60% at 50% 45%, var(--bg-light) 0%, var(--bg-mid) 60%, var(--bg-edge) 100%);
  }
  .board-title {
    position: absolute;
    top: 22px; left: 0; width: 100%;
    text-align: center;
    font-size: 62px;
    font-weight: 600;
    color: var(--title);
    letter-spacing: 1px;
    line-height: 1;
  }
  .dish-photo {
    position: absolute;
    border-radius: 50%;
    box-shadow: 0 2px 4px rgba(0,0,0,0.15);
  }
  .photo-pho { background: radial-gradient(circle at 50% 45%, var(--herb) 0 22%, var(--broth) 40%, var(--bowl) 62%, #222 84%); }
  .photo-salad { background: radial-gradient(circle at 50% 45%, #7a4a2a 0 20%, #d98a3a 38%, var(--herb) 48%, var(--bowl) 64%, #222 86%); }
  .photo-rice { background: radial-gradient(circle at 60% 40%, var(--rice) 0 18%, #7a3a2a 32%, var(--herb) 46%, #ffffff 64%, #f3f3f3 100%); }
  .photo-fried { background: radial-gradient(circle at 50% 50%, var(--fried) 0 40%, #f3e2c8 70%, #ffffff 100%); }
  .photo-stirfry { background: radial-gradient(circle at 50% 50%, #b86a3a 0 24%, var(--herb) 40%, #e39b5a 52%, #ffffff 68%, #222 90%); }
  .photo-spring { background: radial-gradient(circle at 45% 60%, var(--roll-fried) 0 34%, #e3a062 52%, #ffffff 70%, #222 92%); }
  .photo-ricepaper { background: radial-gradient(circle at 50% 55%, var(--roll-fresh) 0 30%, #b9d59a 46%, #f6f6f2 64%, #222 92%); }
  .band {
    position: absolute;
    display: flex;
    background: var(--band);
  }
  .band-cell {
    flex: 1 1 0;
    display: flex;
    align-items: center;
    justify-content: center;
    color: var(--band-text);
    font-weight: 500;
    white-space: nowrap;
    overflow: hidden;
    border-left: 2px solid var(--divider);
  }
  .band-cell:first-child { border-left: none; }
  .band-large .band-cell { font-size: 31px; }
  .band-small .band-cell { font-size: 15px; letter-spacing: 0.3px; }
  .band-small .band-cell.tight { font-size: 12.5px; }
  .band-rolls .band-cell { font-size: 23px; }
</style>
</head>
<body>
<main class="board">
  <h1 class="board-title">Menu Board</h1>

  <!-- Pho -->
  <div class="dish-photo photo-pho" style="left:56px;top:142px;width:144px;height:144px" role="img" aria-label="Photo of beef pho bowl"></div>
  <div class="dish-photo photo-pho" style="left:314px;top:142px;width:144px;height:144px" role="img" aria-label="Photo of chicken pho bowl"></div>
  <div class="dish-photo photo-pho" style="left:572px;top:142px;width:144px;height:144px" role="img" aria-label="Photo of tofu pho bowl"></div>
  <div class="band band-large" style="left:0;top:298px;width:772px;height:54px">
    <div class="band-cell">Beef Pho</div>
    <div class="band-cell">Chicken Pho</div>
    <div class="band-cell">Tofu Pho</div>
  </div>

  <!-- Noodle salads -->
  <div class="dish-photo photo-salad" style="left:46px;top:378px;width:100px;height:100px" role="img" aria-label="Photo of beef noodle salad"></div>
  <div class="dish-photo photo-salad" style="left:239px;top:378px;width:100px;height:100px" role="img" aria-label="Photo of chicken noodle salad"></div>
  <div class="dish-photo photo-salad" style="left:432px;top:378px;width:100px;height:100px" role="img" aria-label="Photo of BBQ pork noodle salad"></div>
  <div class="dish-photo photo-salad" style="left:626px;top:378px;width:100px;height:100px" role="img" aria-label="Photo of tofu noodle salad"></div>
  <div class="band band-small" style="left:0;top:504px;width:772px;height:43px">
    <div class="band-cell">Beef Noodle salads</div>
    <div class="band-cell">Chicken Noodle salads</div>
    <div class="band-cell">BBQ Pork Noodle salads</div>
    <div class="band-cell">Tofu Noodle salads</div>
  </div>

  <!-- Rice -->
  <div class="dish-photo photo-rice" style="left:46px;top:572px;width:100px;height:100px" role="img" aria-label="Photo of beef with rice"></div>
  <div class="dish-photo photo-rice" style="left:239px;top:572px;width:100px;height:100px" role="img" aria-label="Photo of chicken with rice"></div>
  <div class="dish-photo photo-rice" style="left:430px;top:570px;width:104px;height:104px" role="img" aria-label="Photo of tofu with rice"></div>
  <div class="dish-photo photo-fried" style="left:624px;top:570px;width:104px;height:104px" role="img" aria-label="Photo of fried rice"></div>
  <div class="band band-small" style="left:0;top:700px;width:772px;height:42px">
    <div class="band-cell">Beef Rice</div>
    <div class="band-cell">Chicken Rice</div>
    <div class="band-cell">Tofu Rice</div>
    <div class="band-cell">Fried Rice</div>
  </div>

  <!-- Stir fry -->
  <div class="dish-photo photo-stirfry" style="left:46px;top:770px;width:100px;height:100px" role="img" aria-label="Photo of beef stir fry noodles"></div>
  <div class="dish-photo photo-stirfry" style="left:239px;top:770px;width:100px;height:100px" role="img" aria-label="Photo of chicken stir fry noodles"></div>
  <div class="dish-photo photo-stirfry" style="left:432px;top:770px;width:100px;height:100px" role="img" aria-label="Photo of tofu stir fry noodles"></div>
  <div class="dish-photo photo-fried" style="left:626px;top:770px;width:100px;height:100px" role="img" aria-label="Photo of stir fry with thick rice noodles"></div>
  <div class="band band-small" style="left:0;top:895px;width:772px;height:43px">
    <div class="band-cell"></div>
    <div class="band-cell">Chicken StirFry Noodles</div>
    <div class="band-cell">Tofu StirFry Noodles</div>
    <div class="band-cell tight">StirFry with Thick Rice Noodles</div>
  </div>

  <!-- Rolls -->
  <div class="dish-photo photo-spring" style="left:186px;top:967px;width:142px;height:142px" role="img" aria-label="Photo of fried spring rolls with dipping sauce"></div>
  <div class="dish-photo photo-ricepaper" style="left:443px;top:967px;width:142px;height:142px" role="img" aria-label="Photo of fresh ricepaper rolls"></div>
  <div class="band band-rolls" style="left:129px;top:1140px;width:513px;height:58px">
    <div class="band-cell">Spring Rolls</div>
    <div class="band-cell">Ricepaper Rolls</div>
  </div>
</main>
</body>
</html>
```